Willow Ascent Services Business Card Design

I require a business card design for my business Willow Ascent Services. The purpose of this business is to enable people to make positive change in their lives. This business offers life coaching, hypnotherapy and facilitation services. The slogan is 'Rise from the ashes and live the life you want.' Coaching services will be available internationally whilst the hypnotherapy and facilitation services will focus on delivery in south east Queensland.

The business card should be crisp, clean, professional and give the client positive feelings of achieving success.

The logo must be representative of a phoenix rising from the ashes which is a symbol of regeneration and new life. My preference is a black Phoenix on a white background similar to the Phoenix image attached to this brief. I'm happy to see other concepts you have too. The logo and business name must be scalable so it can be printed on a large outdoor sign. Therefore the following files must be provided as a minimum:
-Business card
-Logo on it's own
-Business name on it's own

The following detail must appear on either the front/back of the business card
-Logo
-Willow Ascent Services
-Rise from the ashes and live the life you want.
-Personal and business success through
-Coaching | Hypnotherapy | Facilitation
-Greta Halloway
-Founder

-Life Coach
-Clinical Hypnotherapist
-MBA (Project Management specialisation)
-Neuro Linguistic Programming Practitioner

-0412 835 076
-E: willowascent.au@kestrelmail.com
-www.willow-ascent.com.au
-Contact us now for your free 20min assessment

Please feel free to ask me as many questions as you like :) Thank you.

Hi all,  friendly reminder that the logo needs to be your own design and cannot be a Framequarry or other purchased or free image.  

Thanks heaps
Keep the great designs coming in. You're all so talented.
Greta

• Feedback from older people is that black backgrounds with lighter fonts are difficult to read so please no black backgrounds.

```html
<!DOCTYPE html>
<html lang="en">
<head>
<meta charset="utf-8">
<title>Willow Ascent Services – Business Card</title>
<link rel="stylesheet" href="https://fonts.googleapis.com/css2?family=Arimo:wght@400;700&display=swap">
<style>
  :root {
    --page: #ffffff;
    --card: #ffffff;
    --card-edge: #bdbdbd;
    --band: #ececec;
    --ink: #111111;
    --ink-soft: #444444;
    --icon: #555555;
    --emblem-main: #3a3a3a;
    --emblem-soft: #9a9a9a;
    --ghost-main: #dcdcdc;
    --ghost-soft: #f4f4f4;
  }
  * { box-sizing: border-box; margin: 0; padding: 0; }
  html, body {
    width: 1200px; height: 844px; overflow: hidden;
    background: var(--page);
    font-family: "Arimo", Arial, sans-serif;
  }
  .canvas { position: relative; width: 1200px; height: 844px; }

  .side-label {
    position: absolute;
    font-size: 60px; font-weight: 400; color: var(--ink);
    line-height: 1; transform: translateX(-50%);
  }
  .side-label--front { left: 254px; top: 48px; }
  .side-label--back { left: 831px; top: 190px; }

  /* Front */
  .card-front {
    position: absolute; left: 46px; top: 121px;
    width: 421px; height: 687px;
    background: var(--card); color: var(--ink);
    border: 1px solid var(--card-edge);
  }
  .card-front__phone {
    position: absolute; right: 14px; top: 9px;
    display: flex; align-items: center; gap: 4px;
    font-size: 21px; font-weight: 700;
  }
  .card-front__phone svg { width: 20px; height: 20px; }
  .card-front__emblem {
    position: absolute; left: 95px; top: 30px;
    width: 240px; height: 570px;
    background: radial-gradient(ellipse at 50% 35%, var(--emblem-main) 0%, var(--emblem-soft) 45%, var(--card) 75%);
    border-radius: 50% 50% 40% 40% / 30% 30% 60% 60%;
  }
  .card-front__name {
    position: absolute; left: 0; right: 0; top: 606px;
    text-align: center; font-size: 31px; font-weight: 700; line-height: 36px;
  }
  .card-front__rule {
    position: absolute; left: 0; right: 0; top: 649px;
    height: 2px; background: var(--ink);
  }
  .card-front__tagline {
    position: absolute; left: 0; right: 0; top: 658px;
    text-align: center; font-size: 17px; font-weight: 700; line-height: 20px;
  }

  /* Back */
  .card-back {
    position: absolute; left: 490px; top: 254px;
    width: 686px; height: 421px;
    background: var(--card); color: var(--ink);
    border: 1px solid var(--card-edge);
    overflow: hidden;
  }
  .card-back__header {
    height: 39px; background: var(--band);
    border-bottom: 1px solid var(--card-edge);
    font-size: 24px; font-weight: 700;
    text-align: center; line-height: 38px;
  }
  .card-back__ghost {
    position: absolute; left: 435px; top: 46px;
    width: 250px; height: 330px;
    background: radial-gradient(ellipse at 55% 40%, var(--ghost-main) 0%, var(--ghost-soft) 70%, var(--card) 100%);
    border-radius: 50% 50% 45% 45%;
  }
  .card-back__list {
    position: absolute; left: 20px; top: 59px;
    list-style: none;
  }
  .card-back__list li {
    font-size: 21px; font-weight: 700;
    height: 46px; line-height: 28px;
  }
  .card-back__list li::before { content: "• "; }
  .card-back__footer {
    position: absolute; left: 10px; right: 10px; top: 389px;
    display: flex; justify-content: space-between;
    font-size: 20px; font-weight: 400; color: var(--ink-soft);
  }
  .card-back__contact { display: flex; align-items: center; gap: 8px; }
  .card-back__contact svg { width: 20px; height: 16px; }
</style>
</head>
<body>
<main class="canvas">
  <div class="side-label side-label--front">Front</div>
  <section class="card-front">
    <div class="card-front__phone">
      <svg viewBox="0 0 20 20" aria-hidden="true">
        <circle cx="10" cy="10" r="8.5" fill="none" stroke="#111" stroke-width="1.5"/>
        <path d="M7 5.5c-1 1-1 3.5 1.5 6.5s5 3.5 6 2.5l-1.5-2-1.5.8c-1-.5-2.8-2.5-3-3.5l.8-1.3z" fill="#111"/>
      </svg>
      <span>0412 835 076</span>
    </div>
    <div class="card-front__emblem" role="img" aria-label="Phoenix emblem with spread wings and long flowing tail feathers"></div>
    <div class="card-front__name">Willow Ascent Services</div>
    <div class="card-front__rule"></div>
    <div class="card-front__tagline">Rise from the ashes and live the life you want.</div>
  </section>

  <div class="side-label side-label--back">Back</div>
  <section class="card-back">
    <div class="card-back__header">Contact us now for your free 20min assessment</div>
    <div class="card-back__ghost" role="img" aria-label="Faint phoenix emblem in the background"></div>
    <ul class="card-back__list">
      <li>Personal and business success through</li>
      <li>Coaching | Hypnotherapy | Facilitation</li>
      <li>Greta Halloway MBA specializing in project management</li>
      <li>Founder</li>
      <li>Certified Clinical Hypnotherapist</li>
      <li>Certified Neuro Linguistic Programming Practitioner</li>
      <li>Certified Life Coach</li>
    </ul>
    <div class="card-back__footer">
      <span class="card-back__contact">
        <svg viewBox="0 0 20 16" aria-hidden="true">
          <rect x="1" y="1" width="18" height="14" fill="none" stroke="#555" stroke-width="1.5"/>
          <path d="M1 1l9 8 9-8M1 15l7-6M19 15l-7-6" fill="none" stroke="#555" stroke-width="1.5"/>
        </svg>
        willowascent.au@kestrelmail.com
      </span>
      <span class="card-back__contact">
        <svg viewBox="0 0 20 16" aria-hidden="true">
          <rect x="6" y="2" width="9" height="13" rx="4.5" fill="none" stroke="#555" stroke-width="1.5"/>
          <path d="M10.5 2v5M6 7h9" stroke="#555" stroke-width="1.5"/>
        </svg>
        www.willow-ascent.com.au
      </span>
    </div>
  </section>
</main>
</body>
</html>
```